Business Card Design

New business card design

Target Market(s)

Residential & Commercial Property Managers

Industry/Entity Type

Plumbing Services

Contact Information for Business Card

Name - Owen Tredgold, title - Director, Phone Number - 0431 862 507, email - owen@rvb-plumbing.com.au, Company ABN - 73 215 904 386,

Font styles to use
Sans Serif

Colors
0054AA
0677BA
7BADD7
CADEEF
E8F1F8

```html
<!DOCTYPE html>
<html lang="en">
<head>
<meta charset="utf-8">
<title>RVB Plumbing Services – Business Card</title>
<link href="https://fonts.googleapis.com/css2?family=Saira:wght@300;400;600&display=swap" rel="stylesheet">
<style>
  :root {
    --backdrop: #adadad;
    --card-dark: #2f2f2f;
    --card-light: #ffffff;
    --brand-blue: #00a6e6;
    --logo-grey: #8a8a8a;
    --tag-light: #d8d8d8;
    --ink-dark: #222428;
    --ink-warm: #6b5e55;
    --shadow: rgba(0, 0, 0, 0.35);
  }
  * { margin: 0; padding: 0; box-sizing: border-box; }
  html, body {
    width: 1200px; height: 1000px; overflow: hidden;
    background: var(--backdrop);
    font-family: "Saira", sans-serif;
  }
  .card {
    position: absolute; left: 293px; width: 615px; height: 354px;
    border-radius: 16px;
    box-shadow: 6px 8px 16px var(--shadow);
    overflow: hidden;
    text-align: center;
  }
  .card--front { top: 133px; background: var(--card-dark); }
  .card--back { top: 526px; background: var(--card-light); }

  .brand {
    position: absolute; left: 0; right: 0;
    font-weight: 300;
  }
  .brand__name { display: block; line-height: 1; }
  .brand__tag { display: block; line-height: 1.2; }
  .brand__dot {
    position: absolute; left: 50%;
    border-radius: 50%; background: var(--brand-blue);
  }

  .card--front .brand { top: 116px; color: var(--logo-grey); }
  .card--front .brand__name { font-size: 96px; letter-spacing: 14px; padding-left: 14px; }
  .card--front .brand__tag { font-size: 17px; letter-spacing: 15px; padding-left: 15px; margin-top: 22px; color: var(--tag-light); }
  .card--front .brand__dot { top: 96px; width: 24px; height: 24px; margin-left: -12px; }

  .card--back .brand { top: 50px; color: var(--ink-dark); }
  .card--back .brand__name { font-size: 40px; letter-spacing: 6px; padding-left: 6px; }
  .card--back .brand__tag { font-size: 7px; letter-spacing: 7px; padding-left: 7px; margin-top: 18px; color: var(--ink-warm); }
  .card--back .brand__dot { top: 43px; width: 12px; height: 12px; margin-left: -6px; }

  .abn {
    position: absolute; top: 130px; left: 0; right: 0;
    font-size: 9.5px; letter-spacing: 2px; color: var(--ink-warm);
  }
  .person__name {
    position: absolute; top: 172px; left: 0; right: 0;
    font-size: 22px; font-weight: 600; color: var(--brand-blue);
  }
  .person__title {
    position: absolute; top: 207px; left: 0; right: 0;
    font-size: 9.5px; letter-spacing: 2.5px; color: var(--ink-dark);
  }
  .contact-icons {
    position: absolute; top: 232px; left: 0; right: 0;
    display: flex; justify-content: center; gap: 3px;
  }
  .contact-icons svg { width: 23px; height: 23px; }
  .contact__line {
    position: absolute; left: 0; right: 0; color: var(--ink-warm);
  }
  .contact__phone { top: 259px; font-size: 18px; letter-spacing: 0.5px; }
  .contact__email { top: 281px; font-size: 17px; }
</style>
</head>
<body>
  <section class="card card--front" aria-label="Card front">
    <div class="brand">
      <span class="brand__name">RVB</span>
      <span class="brand__tag">plumbing services</span>
      <span class="brand__dot"></span>
    </div>
  </section>

  <section class="card card--back" aria-label="Card back">
    <div class="brand">
      <span class="brand__name">RVB</span>
      <span class="brand__tag">plumbing services</span>
      <span class="brand__dot"></span>
    </div>
    <p class="abn">ABN - 73 215 904 386</p>
    <p class="person__name">Owen Tredgold</p>
    <p class="person__title">DIRECTOR</p>
    <div class="contact-icons">
      <svg viewBox="0 0 24 24" aria-label="Phone">
        <circle cx="12" cy="12" r="12" fill="var(--brand-blue)"/>
        <path d="M8.6 6.5c.4-.3.9-.2 1.1.2l1.1 2c.2.4.1.8-.2 1.1l-.7.6c.5 1.2 1.4 2.2 2.6 2.8l.6-.7c.3-.3.8-.4 1.1-.2l2 1.1c.4.2.5.7.2 1.1l-.9 1.1c-.4.5-1.1.7-1.7.4-3-1.2-5.2-3.5-6.3-6.4-.2-.6 0-1.3.5-1.7z" fill="#fff"/>
      </svg>
      <svg viewBox="0 0 24 24" aria-label="Email">
        <circle cx="12" cy="12" r="12" fill="var(--brand-blue)"/>
        <rect x="6" y="8" width="12" height="8.5" fill="#fff"/>
        <path d="M6 8l6 4.8L18 8M6 16.5l4.3-4M18 16.5l-4.3-4" fill="none" stroke="var(--brand-blue)" stroke-width="0.9"/>
      </svg>
    </div>
    <p class="contact__line contact__phone">0431 862 507</p>
    <p class="contact__line contact__email">owen@rvb-plumbing.com.au</p>
  </section>
</body>
</html>
```